New Personal and business business card

I need a new business card design for my business and myslef personally. One side is my business and the other side is my personal information.

Contact Information for Business Card

i will include a copy of my current business card

Colors

Designer to choose colors to be used in the design.

Requirements
Must have
• all of the information currently on my card
Should not have
• i prefer not to have gold color. i know the logo has gold but use gray one

```html
<!DOCTYPE html>
<html lang="en">
<head>
<meta charset="utf-8">
<title>Valiant Rotorcraft – Business Cards</title>
<link rel="stylesheet" href="https://fonts.googleapis.com/css2?family=Archivo:wght@700;900&family=Montserrat:wght@400;600&display=swap">
<style>
  :root {
    --backdrop: #b9b9bb;
    --card: #232123;
    --card-edge: #2b292b;
    --silver: #b4b4b6;
    --silver-strong: #c4c4c6;
    --white: #f4f4f4;
    --mint: #1ef0a0;
  }
  * { margin: 0; padding: 0; box-sizing: border-box; }
  html, body {
    width: 1200px; height: 1200px; overflow: hidden;
    background: var(--backdrop);
  }
  .card {
    position: absolute;
    left: 228px;
    width: 746px;
    height: 430px;
    background: linear-gradient(135deg, var(--card-edge), var(--card) 60%);
    box-shadow: 0 4px 8px rgba(0,0,0,0.35);
  }
  .card--business { top: 114px; font-family: "Montserrat", sans-serif; color: var(--silver); }
  .card--personal { top: 583px; font-family: "Archivo", sans-serif; }

  .card--business .holder-name {
    position: absolute; left: 33px; top: 62px;
    font-size: 27px; font-weight: 600; color: var(--silver-strong);
    letter-spacing: 0.2px;
  }
  .card--business .holder-title {
    position: absolute; left: 33px; top: 100px;
    font-size: 18px; font-weight: 400;
  }
  .brand-name {
    position: absolute; right: 33px; top: 70px;
    font-size: 30px; font-weight: 600; color: var(--silver);
    text-align: right;
  }
  .services {
    position: absolute; left: 33px; top: 229px;
    list-style: none; font-size: 18px; line-height: 27px;
  }
  .business-contact {
    position: absolute; right: 33px; top: 337px;
    text-align: right; font-size: 18px; line-height: 27px;
  }

  .personal-name {
    position: absolute; left: 0; right: 0; top: 36px;
    text-align: center; font-weight: 900; font-size: 44px;
    color: var(--mint); letter-spacing: 1px;
  }
  .personal-rule {
    position: absolute; left: 138px; width: 468px; top: 94px;
    height: 3px; background: var(--mint);
  }
  .credentials {
    position: absolute; left: 27px; top: 120px; right: 20px;
    list-style: none; color: var(--white);
    font-weight: 700; font-size: 17.5px; line-height: 30px;
    text-transform: uppercase; letter-spacing: -0.1px;
  }
  .credentials li::before { content: "• "; }
  .personal-email, .personal-phone {
    position: absolute; color: var(--mint); font-weight: 700; font-size: 19.5px;
  }
  .personal-email { left: 27px; top: 370px; }
  .personal-phone { right: 30px; top: 375px; }
</style>
</head>
<body>
  <section class="card card--business">
    <h1 class="holder-name">DALTON REEVES</h1>
    <p class="holder-title">Chief Pilot/Owner</p>
    <p class="brand-name">Valiant Rotorcraft</p>
    <ul class="services">
      <li>Scenic Tours/Event Rides</li>
      <li>Photography</li>
      <li>Flight Instruction-Airplane &amp; Helicopter</li>
      <li>Special Events</li>
      <li>Frost Patrol/Crop Pollination</li>
      <li>Aircraft Sales</li>
    </ul>
    <div class="business-contact">
      <p>PH. 555.014.2870</p>
      <p>WWW.VALIANTROTORCRAFT.COM</p>
    </div>
  </section>

  <section class="card card--personal">
    <h2 class="personal-name">DALTON REEVES</h2>
    <div class="personal-rule"></div>
    <ul class="credentials">
      <li>Designated Pilot Examiner Rotorcraft Helicopter</li>
      <li>CFII Airplane and Helicopter</li>
      <li>MEI,IGI,AGI</li>
      <li>ATP Multiengine Land/ ATP Single Engine Land/ATP Helicopter</li>
      <li>Seaplane Instructor</li>
      <li>Marlow Crest Insurance Check Pilot for Harlan Helicopters</li>
      <li>Contract Pilot and Instructor</li>
      <li>CE-525S, EMB-505 Single Pilot and LR-Jet Type Rating</li>
    </ul>
    <p class="personal-email">DALTON.J.REEVES@SKYMAIL.COM</p>
    <p class="personal-phone">PH:555.013.6642</p>
  </section>
</body>
</html>
```